Wordpress Template/Design for my business

I need a WordPress template to showcase my technical knowledge for my consultancy. Ideally it will use the same formatting your logo that you created for me.

bility to add tabs, and about me section which ill update

good examples:
http://www.plainlymeadowbit.com/
http://lendrickfaulk.com/
http://berttolsmaker.nl/

Target Market(s)

Technical people looking

Industry/Entity Type

Business

Number of Pages Required

3 page

Font styles to use
Other font styles liked:
• See logo

Requirements
Must have
• A

```html
<!DOCTYPE html>
<html lang="en">
<head>
<meta charset="utf-8">
<title>Nimbrel — Cloud Innovation</title>
<link href="https://fonts.googleapis.com/css2?family=Kanit:wght@400;500&family=Lato:ital,wght@0,400;0,700;1,400&family=Questrial&display=swap" rel="stylesheet">
<style>
:root{
  --header:#3a3a3a;
  --header-band:#454545;
  --page:#f4f3f1;
  --brand:#1596d2;
  --brand-bright:#10a3e0;
  --ink:#3b3b3b;
  --panel-head:#343434;
  --line:#d6d6d6;
  --white:#ffffff;
  --footer:#575757;
}
*{margin:0;padding:0;box-sizing:border-box}
html,body{width:1116px;height:1200px;overflow:hidden}
body{position:relative;background:var(--page);font-family:"Lato",sans-serif;color:var(--ink)}
.abs{position:absolute}

.site-header{left:0;top:0;width:1116px;height:113px;background:var(--header)}
.site-header .band{left:0;top:100px;width:1116px;height:13px;background:var(--header-band)}
.brand{left:160px;top:40px;display:flex;align-items:center;gap:8px}
.brand-mark{width:22px;height:22px;border-radius:50%;background:var(--brand)}
.brand-name{font-family:"Kanit",sans-serif;font-weight:500;font-size:28px;color:var(--brand);line-height:1}
.brand-tag{left:184px;top:89px;font-size:11px;color:var(--white);letter-spacing:.3px}
.contact-top{top:20px;display:flex;align-items:center;gap:8px;color:var(--white);font-size:14.5px;font-weight:700}
.contact-top svg{width:26px;height:26px}
.main-nav{right:160px;top:68px;display:flex;height:25px;align-items:center}
.main-nav a{color:var(--white);text-decoration:none;font-size:12px;font-weight:700;padding:0 25px;border-left:1px solid #5b5b5b;line-height:25px}
.main-nav a:first-child{border-left:none}
.main-nav a:last-child{padding-right:0}

.hero{left:0;top:113px;width:1116px;height:266px;background:linear-gradient(90deg,#8a6c5a 0%,#b39180 14%,#5b8ccd 30%,#2a6bbf 55%,#144e9f 80%,#0c3f8c 100%)}
.hero-title{right:160px;top:190px;text-align:right;font-family:"Kanit",sans-serif;font-weight:500;font-size:27px;line-height:35px;color:var(--white)}
.hero-dots{right:160px;top:273px;display:flex;gap:12px}
.hero-dots span{width:12px;height:12px;border-radius:50%;background:var(--white)}
.hero-dots span.active{background:var(--brand-bright);box-shadow:0 0 0 2px var(--white) inset}

.section-title{font-family:"Kanit",sans-serif;font-weight:500;font-size:21px;color:var(--brand);left:160px}
.body-text{font-size:13.3px;line-height:19.8px;letter-spacing:.15px}
.divider{left:160px;width:518px;height:1px;background:var(--line)}
.portrait{left:161px;top:462px;width:127px;height:112px;background:linear-gradient(135deg,#6d8a78,#a88c74 50%,#4a4f52)}
.ticks{left:160px;top:734px;display:grid;grid-template-columns:252px 260px;row-gap:10px;font-size:13.3px}
.ticks li{list-style:none;display:flex;align-items:center;gap:7px;height:19px}
.ticks svg{width:11px;height:11px}
.map{left:161px;top:908px;width:238px;height:168px;background:linear-gradient(160deg,#e9e6df,#dcd8cf);border:3px solid var(--white);box-shadow:0 1px 4px rgba(0,0,0,.25)}
.info{left:418px;font-size:13px;line-height:20px;display:flex;gap:8px}
.info svg{width:12px;height:14px;margin-top:3px;flex:none}

.widget{left:710px;width:246px;background:var(--white);border:1px solid #e1e1e1}
.widget-head{height:39px;background:var(--panel-head);color:var(--white);font-family:"Questrial",sans-serif;font-size:20px;line-height:39px;padding-left:17px}
.search-field{margin:16px 16px;height:32px;border:1px solid #dcdcdc;background:#f7f7f7;font-size:11px;font-style:italic;color:#555;padding-left:9px;line-height:30px;position:relative}
.search-field svg{position:absolute;right:10px;top:9px;width:13px;height:13px}
.socials{display:flex;gap:13px;padding:14px 0 0 24px}
.socials span{width:26px;height:26px;border-radius:50%}
.ads{display:grid;grid-template-columns:99px 99px;gap:14px 13px;padding:15px 0 0 16px}
.ads div{width:99px;height:99px}
.news-title{font-family:"Questrial",sans-serif;font-size:20px;color:#3b3b3b;padding:11px 0 0 14px}
.news-input{margin:16px 0 0 14px;width:213px;height:32px;border:1px solid #d6d6d6;background:#f7f7f7;font-size:11px;font-style:italic;color:#666;padding-left:9px;line-height:30px}
.news-btn{margin:16px 0 0 14px;width:84px;height:32px;background:var(--brand-bright);color:var(--white);font-family:"Kanit",sans-serif;font-weight:500;font-size:12.5px;letter-spacing:.6px;text-align:center;line-height:32px}

.site-footer{left:0;top:1160px;width:1116px;height:40px;background:var(--footer);color:#eaeaea;font-size:11.5px;text-align:center;line-height:40px}
</style>
</head>
<body>

<header class="site-header abs">
  <div class="band abs"></div>
  <div class="brand abs"><span class="brand-mark"></span><span class="brand-name">Nimbrel</span></div>
  <div class="brand-tag abs">cloud innovation</div>
  <div class="contact-top abs" style="left:635px">
    <svg viewBox="0 0 26 26"><circle cx="13" cy="13" r="11.5" fill="none" stroke="#1596d2" stroke-width="2"/><rect x="7.5" y="9" width="11" height="8" fill="#1596d2"/><path d="M7.5 9l5.5 4.5L18.5 9" fill="none" stroke="#3a3a3a" stroke-width="1.2"/></svg>
    <span>info@nimbrel.com</span>
  </div>
  <div class="contact-top abs" style="left:825px">
    <svg viewBox="0 0 26 26"><circle cx="13" cy="13" r="11.5" fill="none" stroke="#1596d2" stroke-width="2"/><rect x="9.5" y="7" width="7" height="12" rx="1.5" fill="none" stroke="#1596d2" stroke-width="1.6"/><rect x="11" y="9" width="4" height="5" fill="#1596d2"/></svg>
    <span>(012) 555 0148</span>
  </div>
  <nav class="main-nav abs"><a href="#">HOME</a><a href="#">ABOUT</a><a href="#">MY EXPERTISE</a><a href="#">CONTACT</a></nav>
</header>

<section class="hero abs" role="img" aria-label="Banner photo: consultant touching a floating cloud interface against a blue sky"></section>
<h1 class="hero-title abs">Lorem Ipsum Dolor Sit Amet<br>Consectetur Adipiscing Elit</h1>
<div class="hero-dots abs"><span class="active"></span><span></span><span></span></div>

<h2 class="section-title abs" style="top:421px">About Marten Hale</h2>
<div class="portrait abs" role="img" aria-label="Portrait photo of the consultant"></div>
<p class="body-text abs" style="left:307px;top:468px;width:368px">Lorem ipsum dolor sit amet, consecit adipiscing elit, sed do eiusmod tempor incidimen labore n dolorme laboris ni ut aliquip ex ena lin consequat Duis aute irure dolor in reprehenderit magna aliqua , conadipi velit sed quia non numquam eius modi tempora incidunt.</p>
<div class="divider abs" style="top:603px"></div>

<h2 class="section-title abs" style="top:618px;left:159px">My Expertise</h2>
<p class="body-text abs" style="left:161px;top:667px;width:515px">Lorem ipsum dolor sit amet, consecit adipiscing elit, sed do eiusmod tempor incidimen labore n dolorme laboris ni ut aliquip a aliqua ipsum quia dolor sit amet, conadipi velit sed quia non numquam eius modi tempora incidunt.</p>
<ul class="ticks abs">
  <li><svg viewBox="0 0 12 12"><path d="M1 6.5l3.2 3.2L11 2.5" fill="none" stroke="#222" stroke-width="2.2"/></svg>Duis aute irure dolor in reprehenderit</li>
  <li><svg viewBox="0 0 12 12"><path d="M1 6.5l3.2 3.2L11 2.5" fill="none" stroke="#222" stroke-width="2.2"/></svg>Duis aute irure dolor in reprehenderit</li>
  <li><svg viewBox="0 0 12 12"><path d="M1 6.5l3.2 3.2L11 2.5" fill="none" stroke="#222" stroke-width="2.2"/></svg>Duis aute irure dolor in reprehenderit</li>
  <li><svg viewBox="0 0 12 12"><path d="M1 6.5l3.2 3.2L11 2.5" fill="none" stroke="#222" stroke-width="2.2"/></svg>Duis aute irure dolor in reprehenderit</li>
  <li><svg viewBox="0 0 12 12"><path d="M1 6.5l3.2 3.2L11 2.5" fill="none" stroke="#222" stroke-width="2.2"/></svg>Duis aute irure dolor in reprehenderit</li>
  <li><svg viewBox="0 0 12 12"><path d="M1 6.5l3.2 3.2L11 2.5" fill="none" stroke="#222" stroke-width="2.2"/></svg>Duis aute irure dolor in reprehenderit</li>
</ul>
<div class="divider abs" style="top:840px"></div>

<h2 class="section-title abs" style="top:856px">Get In Touch</h2>
<div class="map abs" role="img" aria-label="Street map showing the office location"></div>
<div class="info abs" style="top:906px">
  <svg viewBox="0 0 12 14"><path d="M6 13.5S1 8 1 5a5 5 0 0 1 10 0c0 3-5 8.5-5 8.5z" fill="#1596d2"/><circle cx="6" cy="5" r="1.8" fill="#f4f3f1"/></svg>
  <div><b>Nimbrel</b><br>Street Name, City Name,<br>State Name - 123456</div>
</div>
<div class="info abs" style="top:977px">
  <svg viewBox="0 0 12 14"><path d="M2 1.5l2.5-.5 1.3 3-1.5 1.2c.7 1.8 1.8 3.2 3.4 4.2l1.3-1.4 2.8 1.5-.4 2.5C6.5 12.5 1.5 7 2 1.5z" fill="#1596d2"/></svg>
  <div>(012) 555 0148</div>
</div>
<div class="info abs" style="top:1011px">
  <svg viewBox="0 0 12 14"><rect x="3" y="2" width="6" height="3" fill="#1596d2"/><rect x="1" y="5" width="10" height="5" rx="1" fill="#1596d2"/><rect x="3" y="9" width="6" height="3.5" fill="#1596d2" stroke="#f4f3f1" stroke-width=".8"/></svg>
  <div>(012) 555 0148</div>
</div>
<div class="info abs" style="top:1046px">
  <svg viewBox="0 0 12 14"><rect x="0.5" y="3" width="11" height="8" fill="#1596d2"/><path d="M.5 3L6 7.5 11.5 3" fill="none" stroke="#f4f3f1" stroke-width="1"/></svg>
  <div>info@nimbrel.com</div>
</div>

<aside>
  <div class="widget abs" style="top:427px;height:104px">
    <div class="widget-head">Search</div>
    <div class="search-field">Search...
      <svg viewBox="0 0 13 13"><circle cx="5.5" cy="5.5" r="4.3" fill="none" stroke="#1596d2" stroke-width="1.7"/><path d="M8.6 8.6l3.6 3.6" stroke="#1596d2" stroke-width="1.9"/></svg>
    </div>
  </div>
  <div class="widget abs" style="top:555px;height:95px">
    <div class="widget-head">Follow Us On</div>
    <div class="socials">
      <span style="background:#3b5998"></span><span style="background:#3a8fd0"></span><span style="background:#1a76b3"></span><span style="background:#d83a2b"></span><span style="background:#3f8bd6"></span>
    </div>
  </div>
  <div class="widget abs" style="top:674px;height:283px">
    <div class="widget-head">Ads</div>
    <div class="ads">
      <div role="img" aria-label="Advertisement banner, green" style="background:linear-gradient(#1f7d2e,#135a1f)"></div>
      <div role="img" aria-label="Advertisement banner, blue" style="background:linear-gradient(#1a8fe0,#0f6fc0)"></div>
      <div role="img" aria-label="Advertisement banner, dark with blue strip" style="background:linear-gradient(#3a3a3a 0%,#555 40%,#1d8fd6 45%,#1d8fd6 80%,#1b1b1b 80%)"></div>
      <div role="img" aria-label="Advertisement banner, dark red" style="background:linear-gradient(135deg,#4a1f22,#2a1718)"></div>
    </div>
  </div>
  <div class="widget abs" style="top:982px;height:153px">
    <div class="news-title">Sign Up For Newsletter</div>
    <div class="news-input">Enter your email address</div>
    <div class="news-btn">SUBMIT</div>
  </div>
</aside>

<footer class="site-footer abs">Copyright © 2016 NIMBREL. All Rights Reserved.</footer>

</body>
</html>
```